Wordpress Design Project

Hi,

I would like a more modern colourful design doing for my website Zyl Pando (www.zy%lpando.com - remove percentage). But I do still want to keep the same sort of colors, just maybe lighter. More interesting.

I want the inside pages to NOT all look the same with just boring text.

I want the site to look more appealing and maybe a new logo.
Updates

I would like to mention I would prefer to keep the same logo after rethinking it (possibly a slight refresh of the logo if you feel its a good idea) and the same color scheme as at present.

Saves us rebranding a lot of our apps, tools online ads etc.

Also I thought it is worth mentioning we have 2 parts to the site. The front end and the logged in area. It would be good if when making the front end you keep in mind the back end at http://p.zy%lpando.com (remove percentage). We can only edit this limitedly (can edit the entire footer, the logo and full CSS of it). Would be good if we could make sure the header and footer can be used on the back end as well maybe to make it match.

I also want layouts making not just for the homepage. Obviously every page will basically be the same but I don't want all the other pages to just be 'text' and no real layout.

You can see out main pages on the website at the moment, I want those other pages to be laid out nice and differently as well. For example the testimonials page could be more interesting with speech bubbles and pictures of each person (just use placeholders). The affiliates page could be a description and then a nice fancy list of features why to join etc. 

Nothing overly complicated but I think it makes the whole site seem a lot better.

Target Market(s)

Affiliate Marketing. International.

Requirements
Must have
• Needs to be more room for links across the navigation at the top, also sub menus (at present we have a lot of pages which are hidden deep within other pages).
Nice to have
• Lists of features for advertisers and affiliates on the homepage part.

Menu items and buttons have nice hover over effects.

I want to get across on our pages all the different unique features we have.

Maybe some kind of slider which has past offer logos in, just use example logos.

```html
<!DOCTYPE html>
<html lang="en">
<head>
<meta charset="utf-8">
<title>Zyl Pando – International CPA Affiliate Network</title>
<link href="https://fonts.googleapis.com/css2?family=Roboto:wght@400;700;900&display=swap" rel="stylesheet">
<style>
:root{
  --sky:#2a8fd8;
  --sky-light:#5cb8f0;
  --navy:#0d2f55;
  --navy-deep:#08203c;
  --orange:#f28a16;
  --orange-light:#ffb347;
  --red:#d8262a;
  --text:#444;
  --muted:#777;
  --panel:#eef5fb;
  --white:#fff;
}
*{box-sizing:border-box;margin:0;padding:0}
html,body{width:763px;height:1200px;overflow:hidden}
body{font-family:"Roboto",Arial,sans-serif;color:var(--text);background:#dfeaf3;position:relative;font-size:9px;line-height:1.35}
.header{position:absolute;left:0;top:0;width:763px;height:140px;background:linear-gradient(180deg,var(--sky-light),var(--sky) 70%,#1f77bd)}
.brand{position:absolute;left:60px;top:22px;color:var(--white);font-weight:900;font-size:34px;letter-spacing:1px}
.brand-tag{position:absolute;left:62px;top:62px;color:#d8efff;font-size:9px;letter-spacing:2px}
.follow{position:absolute;right:40px;top:0;height:30px;background:var(--red);border-radius:0 0 6px 6px;display:flex;align-items:center;gap:6px;padding:0 10px;color:var(--white);font-weight:700;font-size:10px}
.follow span.sq{width:16px;height:16px;background:var(--white);opacity:.85;border-radius:3px}
.phone{position:absolute;right:40px;top:50px;color:var(--white);font-size:20px;font-weight:700;display:flex;align-items:center;gap:8px}
.nav{position:absolute;left:60px;top:112px;width:643px;height:28px;background:linear-gradient(var(--orange-light),var(--orange));border-radius:6px 6px 0 0;display:flex;padding:4px 6px 0;gap:4px}
.nav a{color:var(--white);text-decoration:none;font-size:10px;padding:5px 12px;border-radius:4px 4px 0 0}
.nav a.active{background:var(--sky);}
.hero{position:absolute;left:0;top:140px;width:763px;height:370px;background:radial-gradient(ellipse at 50% 45%,#2e78b8,#0f3766 60%,#081f3d)}
.hero-art{position:absolute;left:100px;top:20px;width:563px;height:300px;background:linear-gradient(180deg,#4a90c8,#1c4f85);border-radius:6px;opacity:.8}
.callout{position:absolute;left:180px;top:236px;width:400px;height:64px;background:rgba(8,32,60,.85);border-left:4px solid var(--orange);padding:10px 14px}
.callout h2{color:var(--white);font-size:15px;font-weight:700;text-transform:uppercase}
.callout .btn{display:inline-block;margin-top:6px;background:var(--orange);color:var(--white);font-size:9px;font-weight:700;padding:4px 12px;border-radius:3px;text-transform:uppercase}
.dots{position:absolute;left:0;width:763px;top:344px;display:flex;justify-content:center;gap:6px}
.dots i{width:8px;height:8px;border-radius:50%;background:#9cc6e8}
.dots i.on{background:var(--orange)}
.page{position:absolute;left:40px;top:528px;width:683px;height:490px;background:var(--white);border-radius:6px}
.intro{position:absolute;left:14px;top:12px;width:450px}
.intro h1{color:var(--orange);font-size:15px;font-weight:700;margin-bottom:8px}
.intro p{font-size:8.5px;margin-bottom:7px;color:var(--text)}
.login{position:absolute;right:14px;top:10px;width:196px;height:150px;border:1px solid #f5b46a;border-radius:6px;background:linear-gradient(#fff3e4,#ffe1bd)}
.login h3{background:linear-gradient(var(--orange-light),var(--orange));color:var(--white);text-align:center;font-size:12px;padding:7px 0;border-radius:6px 6px 0 0}
.login label{display:flex;align-items:center;justify-content:space-between;padding:7px 14px 0;font-size:9px;color:var(--red);font-weight:700}
.login label span.field{width:100px;height:16px;background:var(--white);border:1px solid #ccc}
.login .go{margin:8px 0 0 100px;width:44px;height:16px;background:#eee;border:1px solid #bbb;font-size:8px;text-align:center;line-height:14px}
.login .reg{position:absolute;bottom:8px;left:0;width:100%;text-align:center;font-size:9px;font-weight:700;color:var(--red)}
.login .reg b{color:var(--orange)}
.card{position:absolute;top:176px;width:225px;height:126px;border:1px solid #cfe0ee;border-radius:5px;background:var(--panel);padding:10px}
.card h4{font-size:10px;color:var(--navy);margin-bottom:5px;text-transform:uppercase}
.card p{font-size:8px;color:var(--muted)}
.card .signup{position:absolute;left:50%;transform:translateX(-50%);bottom:10px;background:linear-gradient(var(--sky-light),var(--sky));color:var(--white);font-weight:700;font-size:10px;padding:5px 26px;border-radius:4px}
.clients{position:absolute;left:8px;top:316px;width:460px;height:138px;border:1px solid #f5b46a;border-radius:6px;overflow:hidden}
.clients h4{background:linear-gradient(var(--orange-light),var(--orange));color:var(--white);font-size:10px;padding:6px 10px}
.client-row{display:flex;align-items:center;justify-content:space-around;height:100px;padding:0 6px}
.client-row .arr{width:16px;height:16px;border-radius:50%;background:var(--sky)}
.client-row span{font-size:12px;font-weight:700;color:var(--navy)}
.services{position:absolute;right:8px;top:178px;width:200px;height:276px;border:1px solid #9cc6e8;border-radius:6px;background:var(--panel);overflow:hidden}
.services h3{background:linear-gradient(var(--sky-light),var(--sky));color:var(--white);text-align:center;font-size:12px;padding:7px 0}
.svc{display:flex;justify-content:space-between;align-items:center;padding:9px 12px;border-bottom:1px solid #d5e4f0}
.svc b{display:block;font-size:9px;color:var(--red);text-transform:uppercase}
.svc small{font-size:8px;color:var(--muted)}
.svc i{width:32px;height:32px;border-radius:50%;background:var(--sky-light)}
.footer{position:absolute;left:0;top:1030px;width:763px;height:170px;background:var(--navy)}
.fcols{display:flex;gap:0;padding:14px 60px 0}
.fcols ul{list-style:none;width:160px}
.fcols li{color:#c9dcef;font-size:8px;margin-bottom:4px}
.copy{position:absolute;bottom:0;width:100%;height:24px;background:var(--navy-deep);color:#9fb6cd;text-align:center;font-size:8px;line-height:24px}
</style>
</head>
<body>
<header class="header">
  <div class="brand">ZYL PANDO</div>
  <div class="brand-tag">EARN MONEY &amp; INCREASE SALES</div>
  <div class="follow">FOLLOW US <span class="sq"></span><span class="sq"></span><span class="sq"></span></div>
  <div class="phone">
    <svg width="18" height="18" viewBox="0 0 24 24"><path fill="#fff" d="M6.6 10.8a15 15 0 0 0 6.6 6.6l2.2-2.2a1 1 0 0 1 1-.25 11.4 11.4 0 0 0 3.6.57 1 1 0 0 1 1 1V20a1 1 0 0 1-1 1A17 17 0 0 1 3 4a1 1 0 0 1 1-1h3.5a1 1 0 0 1 1 1c0 1.25.2 2.45.57 3.57a1 1 0 0 1-.25 1z"/></svg>
    +44 (0)1200 555019
  </div>
  <nav class="nav">
    <a class="active">Home</a><a>About Us</a><a>Our Blog</a><a>Testimonials</a><a>Affiliates</a><a>Advertisers</a><a>FAQs</a><a>Contact Us</a>
  </nav>
</header>

<section class="hero">
  <div class="hero-art" role="img" aria-label="Globe and network of laptops illustrating an international affiliate network"></div>
  <div class="callout">
    <h2>International Affiliate Network</h2>
    <span class="btn">Join us today</span>
  </div>
  <div class="dots"><i class="on"></i><i></i><i></i><i></i><i></i></div>
</section>

<main class="page">
  <div class="intro">
    <h1>Zyl Pando: International CPA Affiliate Network</h1>
    <p>Welcome to the Zyl Pando affiliate network. On time payments, hot exclusive CPA/CPM offers, fast support and low fees for advertisers, is the making of a leading affiliate network!</p>
    <p>Zyl Pando offer a wide range of advertisers for your websites. So you can start monetizing your traffic or get an additional revenue stream today.</p>
    <p>With Zyl Pando the affiliate network we focus on lead generation offers. We have a range of competitions, surveys, incentives and gambling offers. Whatever the industry, you will be able to find offers to suit your traffic.</p>
    <p>Zyl Pando is a powerful performance-based internet marketing network dedicated to advertisers and affiliates through its powerful affiliate network.</p>
  </div>

  <div class="login">
    <h3>ACCOUNT LOGIN</h3>
    <label>Email <span class="field"></span></label>
    <label>Password <span class="field"></span></label>
    <div class="go">Login</div>
    <div class="reg">NOT REGISTERED? <b>SIGN UP NOW</b></div>
  </div>

  <div class="card" style="left:8px">
    <h4>Affiliates</h4>
    <p>Get access to a wide range of top performing offers for your websites and email marketing lists. Fresh and exclusive offers to promote, join over 1,000 affiliates already signed up.</p>
    <span class="signup">SIGN UP</span>
  </div>
  <div class="card" style="left:243px">
    <h4>Advertisers</h4>
    <p>Generate sales/leads to your website instantly with the Zyl Pando affiliate network. Only pay on performance, no monthly or setup fees. We take the risk out of advertising.</p>
    <span class="signup">SIGN UP</span>
  </div>

  <div class="clients">
    <h4>OUR CLIENTS</h4>
    <div class="client-row">
      <i class="arr"></i>
      <span>Alvo</span><span>Danvix</span><span>Railvento</span><span>Quorelli</span><span>Tovra</span>
      <i class="arr"></i>
    </div>
  </div>

  <aside class="services">
    <h3>ZYL SERVICES</h3>
    <div class="svc"><div><b>Mobile Stats</b><small>Official Zyl Pando Mobile Website</small></div><i></i></div>
    <div class="svc"><div><b>Kestrel Browser</b><small>Official Zyl Pando Extension</small></div><i></i></div>
    <div class="svc"><div><b>Marlin Browser</b><small>Official Zyl Pando Extension</small></div><i></i></div>
    <div class="svc"><div><b>Nimbus OS App</b><small>Official Zyl Pando App</small></div><i></i></div>
  </aside>
</main>

<footer class="footer">
  <div class="fcols">
    <ul><li>Home</li><li>About</li><li>Blog</li><li>Contact</li><li>FAQs</li></ul>
    <ul><li>Affiliate Terms &amp; Conditions</li><li>Advertiser Terms &amp; Conditions</li><li>Privacy Policy &amp; Cookies</li><li>Sign In</li><li>Register</li></ul>
    <ul><li>Connect in Chatterly</li><li>Connect in Peeply</li><li>Connect in Viewtube</li></ul>
    <ul><li>Zyl Pando Ltd</li><li>12 Harbour Row, Suite 4</li><li>Lancaster, United Kingdom</li><li>Tel: +44 (0)1200 555019</li><li>hello@zylpando.example</li></ul>
  </div>
  <div class="copy">© 2013 Zyl Pando Media Ltd - All Rights Reserved.</div>
</footer>
</body>
</html>
```